i am creating an a new cold brew coffee and need a standard format for 5 different flavours. the PDF with 5 colours is what i created as a format and the one page PDF is the style i like but am happy yo move away from it.. the images are the style i like

i am looking for a nice clean tidy but standard out label that will pop off a brown paper backing.

Target Market(s)

18-40 Yr old coffee lovers wanting a high end cold brew coffee

Font styles to use
Serif
Sans Serif

Colors

Designer to choose colors to be used in the design.

Requirements
Must have
• i want a standard format that a component can change colour with flavours, brown paper background. i need the nutritional content box at the back ( as per PDF ) and i would like the text added also, as this is a description of the product
Nice to have
• i like the tidy clinical look of the font pharma bold condensed
• the PDF's show the flavours.. the one with a brown background is something i have seen that i like and the images are the styles i like .

```html
<!DOCTYPE html>
<html lang="en">
<head>
<meta charset="utf-8">
<title>Meridian Brews – Sparkling Citrus Cold Brew Label</title>
<link href="https://fonts.googleapis.com/css2?family=Archivo+Black&family=Dosis:wght@500;600&family=Montserrat:wght@700;800;900&family=Open+Sans+Condensed:wght@300;700&family=Open+Sans:wght@400;600&family=Saira+Semi+Condensed:wght@600&display=swap" rel="stylesheet">
<style>
  :root {
    --paper-light: #ecd3a6;
    --paper-mid: #e2c28e;
    --paper-dark: #d8b47c;
    --flavour: #fbb42a;
    --flavour-soft: #f6d3a2;
    --white: #ffffff;
    --ink: #4d4d4f;
    --ink-brown: #5b4637;
    --ink-deep: #2f2540;
    --rule: #555557;
    --bleed: #2aa9e0;
    --crop: #231f20;
  }
  * { box-sizing: border-box; margin: 0; padding: 0; }
  html, body { width: 1200px; height: 615px; overflow: hidden; background: var(--white); }
  body { position: relative; font-family: "Open Sans", Arial, sans-serif; color: var(--ink); }

  .crop-marks { position: absolute; inset: 0; }
  .label { position: absolute; left: 56px; top: 56px; width: 1088px; height: 502px; border: 2px solid var(--bleed); overflow: hidden; }
  .paper { background: radial-gradient(ellipse at 40% 40%, var(--paper-light), var(--paper-mid) 60%, var(--paper-dark)); }
  .panel { position: absolute; top: 0; height: 100%; }
  .panel-back { left: 0; width: 290px; }
  .strip-word { left: 290px; width: 129px; background: var(--flavour); }
  .panel-front { left: 419px; width: 343px; background: var(--white); }
  .panel-story { left: 762px; width: 268px; }
  .strip-refund { left: 1030px; width: 58px; background: var(--flavour); }

  /* back panel */
  .nutrition { position: absolute; left: 44px; top: 22px; width: 188px; height: 272px; background: var(--white); border: 2px solid var(--ink-deep); padding: 6px 8px; font-family: "Open Sans Condensed", "Arial Narrow", sans-serif; font-size: 10.5px; }
  .nutrition h2 { font-family: "Archivo Black", Arial, sans-serif; font-size: 19px; line-height: 18px; color: var(--rule); font-weight: 400; }
  .nutrition .bar { height: 8px; background: var(--rule); margin: 4px 0 5px; }
  .nutrition .row { display: flex; justify-content: space-between; border-bottom: 1px solid var(--rule); height: 15.6px; align-items: center; }
  .nutrition .row.thick { border-bottom-width: 2px; }
  .nutrition .row.indent { padding-left: 3px; }
  .nutrition .row b { font-weight: 700; }
  .nutrition .row .mid { flex: 1; padding-left: 30px; }
  .nutrition .note { font-family: "Open Sans", Arial, sans-serif; font-size: 7.5px; line-height: 9px; margin-top: 4px; }
  .nutrition .small { font-size: 8.5px; font-weight: 700; }

  .back-copy { position: absolute; left: 44px; top: 302px; width: 210px; font-family: Montserrat, Arial, sans-serif; font-weight: 700; font-size: 10px; line-height: 11px; color: var(--ink-brown); }
  .back-copy p + p { margin-top: 9px; }
  .badges { position: absolute; left: 78px; top: 408px; display: flex; gap: 38px; }
  .badge { width: 60px; text-align: center; font-family: Dosis, Arial, sans-serif; font-weight: 600; font-size: 12px; line-height: 12px; color: var(--ink-brown); }
  .badge svg { display: block; margin: 0 auto 3px; }

  /* flavour strip word */
  .strip-word .word { position: absolute; left: 64px; top: 228px; transform: translate(-50%, -50%) rotate(-90deg); font-family: Montserrat, Arial, sans-serif; font-weight: 900; font-size: 118px; letter-spacing: 4px; color: var(--flavour-soft); white-space: nowrap; }

  /* front panel */
  .front-paper { position: absolute; left: 0; top: 22px; width: 100%; height: 242px; }
  .brand-name { position: absolute; left: 0; width: 100%; top: 118px; text-align: center; font-family: Dosis, Arial, sans-serif; font-weight: 600; font-size: 41px; color: var(--ink); letter-spacing: 1px; }
  .flavour-band { position: absolute; left: 0; top: 264px; width: 100%; height: 84px; background: var(--flavour); }
  .flavour-name { position: absolute; left: 0; width: 100%; top: 278px; text-align: center; font-family: "Saira Semi Condensed", "Arial Narrow", sans-serif; font-weight: 600; font-size: 42px; color: var(--white); letter-spacing: 0.5px; }
  .type-tag { position: absolute; left: 90px; top: 344px; width: 165px; height: 32px; border: 4px solid var(--ink-deep); background: var(--paper-mid); text-align: center; line-height: 24px; font-size: 14px; color: var(--ink-deep); }
  .origin { position: absolute; left: 0; width: 100%; top: 398px; text-align: center; }
  .origin .big { font-size: 22px; line-height: 26px; }
  .origin .sub { font-size: 15.5px; line-height: 20px; }
  .volume { position: absolute; left: 0; width: 100%; top: 462px; text-align: center; font-size: 16px; }

  /* story panel */
  .story { position: absolute; left: 27px; top: 38px; width: 232px; font-family: Montserrat, Arial, sans-serif; font-weight: 700; font-size: 11.6px; line-height: 15px; color: var(--ink-brown); }
  .story p + p { margin-top: 15px; }
  .story .center { text-align: center; }

  .strip-refund .refund { position: absolute; left: 29px; top: 250px; transform: translate(-50%, -50%) rotate(-90deg); font-family: Montserrat, Arial, sans-serif; font-weight: 800; font-size: 15px; color: var(--white); white-space: nowrap; letter-spacing: 0.3px; }
</style>
</head>
<body>
  <svg class="crop-marks" width="1200" height="615" aria-hidden="true">
    <g stroke="var(--crop)" stroke-width="2.5">
      <line x1="14" y1="56" x2="50" y2="56"/><line x1="14" y1="558" x2="50" y2="558"/>
      <line x1="1150" y1="56" x2="1186" y2="56"/><line x1="1150" y1="558" x2="1186" y2="558"/>
      <line x1="56" y1="14" x2="56" y2="50"/><line x1="1144" y1="14" x2="1144" y2="50"/>
      <line x1="56" y1="566" x2="56" y2="602"/><line x1="1144" y1="566" x2="1144" y2="602"/>
    </g>
  </svg>

  <div class="label">
    <section class="panel panel-back paper">
      <div class="nutrition">
        <h2>Nutritional<br>Information</h2>
        <div class="bar"></div>
        <div class="row thick"><span>Serving Size 1 (300ml)</span><span class="small">% Daily Value*</span></div>
        <div class="row thick"><b class="small">Average Per Serving</b></div>
        <div class="row" style="border:none"><b>Calories 100g</b><span>Calories from Fat 00</span></div>
        <div class="row"><b>Energy</b><b>0%</b></div>
        <div class="row indent"><span>Protein</span><b>0%</b></div>
        <div class="row indent"><span>Fat Total 0g</span><b>0%</b></div>
        <div class="row"><span>- Saturated 0g</span><b>0%</b></div>
        <div class="row"><b>Carbs</b><b>0%</b></div>
        <div class="row indent"><span>- sugars</span><span class="mid">0mg</span><b>0%</b></div>
        <div class="row indent"><span>Sodium</span><span class="mid">0g</span><b>0%</b></div>
        <div class="bar" style="margin-top:6px"></div>
        <p class="note">Significant source of Vitamin A and C, Calcium and Iron. *Percent Daily Values are based on a 2000 calorie diet.</p>
      </div>

      <div class="back-copy">
        <p>All Organic Ingredients:Cold Brew coffee, Arabica Beans, Raw Coconut Nectar, Ginger 4%</p>
        <p>• Keep Refrigerated after opening &amp; consume within 2 days from opening</p>
        <p>• Please do not shake</p>
      </div>

      <div class="badges">
        <div class="badge">
          <svg width="38" height="38" viewBox="0 0 38 38"><circle cx="19" cy="19" r="17" fill="none" stroke="var(--ink-brown)" stroke-width="2.5"/></svg>
          Naturally<br>Vegan
        </div>
        <div class="badge">
          <svg width="38" height="38" viewBox="0 0 38 38"><circle cx="19" cy="19" r="17" fill="none" stroke="var(--ink-brown)" stroke-width="2.5"/></svg>
          Gluten<br>Free
        </div>
      </div>
    </section>

    <section class="panel strip-word"><span class="word">Coffee</span></section>

    <section class="panel panel-front">
      <div class="front-paper paper"></div>
      <div class="brand-name">Meridian Brews</div>
      <div class="flavour-band"></div>
      <div class="flavour-name">Sparkling Citrus</div>
      <div class="type-tag">COLD BREW COFFEE</div>
      <div class="origin"><div class="big">100% Australian</div><div class="sub">Made &amp; Owned</div></div>
      <div class="volume">330ml</div>
    </section>

    <section class="panel panel-story paper">
      <div class="story">
        <p>Meridian Brews made this Cold brew coffee to make you think clearer, feel motivated and to just be a better person.</p>
        <p>We won’t claim any responsibility for the achievements you make while drinking our brews, that brilliance was always about you, we just helped you bring it out.</p>
        <p>We know that if you have finished the bottle you will be feeling too good to be reading this label in its entirety. So we will finish it here so you can continue on your motivated way.</p>
        <p>Want to contact us? Sure do it here:<br><span class="center" style="display:block">www.meridianbrews.com.au</span></p>
        <p>Or here: 42 Larkin Lane, Fernvale NSW 2150 or on this 0400 118 204</p>
        <p class="center">World first release:<br>Call 0400 27 27 90<br>For distribution enquiries.</p>
      </div>
    </section>

    <section class="panel strip-refund"><span class="refund">10C REFUND AT COLLECTION DEPOTS #xxxxxx</span></section>
  </div>
</body>
</html>
```